Website for a company offering full serivce charging solutions for electric cars

The company "mero-kant" (english: "mero-edge") offering all-in-one-solutions for charging infrastructure for electric mobility.

There are four products:
1- Wallboxes for single-family homes
2- Solutions for property devloper/-management for property parking space
3- All-in-one-charging solution for municipalities/communities
4- Solutions for tourism/hotels/holiday appartments

The Website structure:
1. Main Page
2.1. Product Page Single Homes
2.2. Product Page Property Management / Parking
2.3. Product Page Municipality
2.4. Product Page Tourism
3. Contact Form / Request for information
4. Imprint / Legal

The Website should be built on Wordpress with a powerful possibility to simply add/modify specific landing pages.

We would like you to implement the website later and also maintain it if possible, but we would be able to do minor modifications by ourselfs (for A/B-Testing)

The website should be clear and simple, easy to understand.
Target group is mainly B2C without deeper knowledge of that topic.

It should suggest, that we will provide a very simple way to get the charging infrastructure done.

We need a contact form, maybe we will use Hubspot later.

Attached you will find a draft of the main page and a landing page (for 2.2) - it is just the content, please ignore the design. We would love to let you create a suitable design.
Also you will find some drafts a bit different for the same story.

I added also a few stock photos, but they don't need to be used! If you have better ideas, you are welcome!

Industry/Entity Type

Charging/Electric mobility

Number of Pages Required

2 page

Font styles to use
Sans Serif

Requirements
Must have
• Based on Wordpress, and the designer should be able to implement it on Wordpress on a later step

```html
<!DOCTYPE html>
<html lang="de">
<head>
<meta charset="utf-8">
<title>mero-kant – Ladelösungen für E-Fahrzeuge</title>
<link href="https://fonts.googleapis.com/css2?family=Comfortaa:wght@700&family=Poppins:wght@400;600;700&display=swap" rel="stylesheet">
<style>
:root{
  --magenta:#e00fb1;
  --ink:#111111;
  --text:#444444;
  --lavender:#f0eef9;
  --white:#ffffff;
  --black:#000000;
}
*{margin:0;padding:0;box-sizing:border-box}
html,body{width:1200px;height:3310px;overflow:hidden}
body{font-family:"Poppins",sans-serif;color:var(--text);background:var(--white);position:relative}
.display{font-family:"Comfortaa",sans-serif;font-weight:700;color:var(--ink)}
.accent{color:var(--magenta)}
.btn{display:inline-block;background:var(--magenta);color:var(--white);font-weight:700;font-size:17px;letter-spacing:.3px;padding:10px 17px;border-radius:6px;text-decoration:none}

/* hero */
.hero{position:absolute;left:0;top:0;width:1200px;height:600px;
  background:linear-gradient(180deg,#4c4862 0%,#3b3a4f 45%,#24232c 100%)}
.hero-photo{position:absolute;left:0;top:0;width:520px;height:600px;
  background:linear-gradient(100deg,#c9c9d2 0%,#8f90a0 55%,rgba(80,78,100,0) 100%)}
.brand{position:absolute;left:112px;top:82px;display:flex;align-items:center;gap:8px;color:var(--white);font-family:"Comfortaa",sans-serif;font-weight:700;font-size:22px}
.brand-dot{width:12px;height:12px;border-radius:50%;background:var(--white)}
.main-nav{position:absolute;top:64px;left:397px;display:flex;gap:44px}
.main-nav a{color:var(--white);font-weight:700;font-size:18px;text-decoration:none;text-transform:uppercase}
.main-nav a.active{color:var(--magenta)}
.hero-copy{position:absolute;left:564px;top:196px;width:540px}
.hero-copy h1{font-family:"Comfortaa",sans-serif;font-weight:700;color:var(--white);font-size:64px;line-height:66px}
.hero-copy p{color:var(--white);font-size:13.5px;line-height:22px;margin:20px 0 28px 4px}
.hero-copy .btn{margin-left:4px}

/* intro */
.intro{position:absolute;left:0;top:600px;width:1200px;height:585px}
.intro h2{position:absolute;left:117px;top:95px;font-size:38px}
.intro .copy{position:absolute;left:119px;top:163px;width:480px;font-size:13.5px;line-height:22.5px}
.intro .copy p+p{margin-top:24px}
.intro .btn{position:absolute;left:119px;top:415px}
.intro-visual{position:absolute;left:664px;top:56px;width:420px;height:420px;border-radius:50%;border:3px solid var(--magenta);padding:8px}
.intro-visual div{width:100%;height:100%;border-radius:50%;background:linear-gradient(160deg,#7f6fe0,#4a32c4)}
.intro-object{position:absolute;left:620px;top:262px;width:230px;height:240px;border-radius:40px 40px 20px 20px;background:linear-gradient(160deg,#ffffff,#dcdce4)}

/* segments */
.segment{position:absolute;left:0;width:1200px;height:526px;background:var(--lavender)}
.segment .photo{position:absolute;top:0;height:526px}
.segment .content{position:absolute}
.segment h3{font-size:27px;margin-bottom:22px}
.checklist{list-style:none;font-size:13.5px;line-height:24px}
.checklist>li{position:relative;padding-left:29px;margin-bottom:14px}
.checklist>li::before{content:"";position:absolute;left:0;top:5px;width:14px;height:14px;border-radius:50%;border:2px solid var(--ink);box-sizing:border-box;
  background:radial-gradient(circle,var(--ink) 0 3px,transparent 3.5px)}
.sublist{list-style:none;margin-top:10px;margin-left:0}
.sublist li{position:relative;padding-left:22px;margin-bottom:8px}
.sublist li::before{content:"";position:absolute;left:0;top:9px;width:9px;height:9px;border-radius:50%;background:var(--ink)}
.segment .btn{margin-top:10px}

.private{top:1185px}
.private .photo{left:0;width:686px;background:linear-gradient(120deg,#eaeaea 0%,#9b8f82 45%,#3d4a63 75%,#6f7b86 100%)}
.private .content{left:767px;top:84px;width:360px}
.business{top:1710px}
.business .photo{left:514px;width:686px;background:linear-gradient(110deg,#8c9392 0%,#c9cfcd 40%,#7f8a8a 70%,#4b4f52 100%)}
.business .content{left:77px;top:50px;width:380px}
.community{top:2236px}
.community .photo{left:0;width:686px;background:linear-gradient(180deg,#b9cfdf 0%,#8ea6b5 35%,#3d4b62 65%,#3a3b45 100%)}
.community .content{left:767px;top:82px;width:360px}

/* products */
.products{position:absolute;left:0;top:2762px;width:1200px;height:313px}
.products h2{position:absolute;left:0;width:1200px;top:52px;text-align:center;font-size:38px}
.product-cards{position:absolute;left:72px;top:128px;display:flex;gap:27px}
.product-card{width:243px;height:112px;background:var(--white);box-shadow:0 2px 14px rgba(0,0,0,.09);display:flex;align-items:center;justify-content:center;text-align:center;
  font-weight:700;font-size:18px;line-height:24px;color:var(--ink);text-transform:uppercase;padding:0 14px;word-break:break-all}

/* footer */
.site-footer{position:absolute;left:0;top:3075px;width:1200px;height:235px;background:var(--black);color:var(--white);text-align:center}
.footer-nav{display:flex;justify-content:center;gap:58px;margin-top:79px}
.footer-nav a{color:var(--white);font-weight:700;font-size:16px;text-decoration:none;text-transform:uppercase}
.copyright{font-size:16px;margin-top:24px}
.social{display:flex;justify-content:center;gap:16px;margin-top:22px}
.social span{width:27px;height:27px;border-radius:50%;background:var(--white)}
</style>
</head>
<body>

<header class="hero">
  <div class="hero-photo" role="img" aria-label="Ladekabel steckt in einem Elektroauto vor einer Stadtsilhouette"></div>
  <div class="brand"><span class="brand-dot"></span>mero-kant.de</div>
  <nav class="main-nav">
    <a class="active" href="#">Lösungen</a>
    <a href="#">Unternehmen</a>
    <a href="#">Services</a>
    <a href="#">Karriere</a>
    <a href="#">Kontakt</a>
  </nav>
  <div class="hero-copy">
    <h1>mero-kant ist Ihr Partner</h1>
    <p>Wir bieten Lösungen sowohl für Privatkunden, Geschäftskunden als auch Kommunen an, die schnell, fair und ohne Eigenleistung zu einer smarten Ladelösung für E-Fahrzeuge kommen möchten.</p>
    <a class="btn" href="#">KONTAKT</a>
  </div>
</header>

<section class="intro">
  <h2 class="display">Unternehmen <span class="accent">Mero-Kant</span></h2>
  <div class="copy">
    <p>Wir bieten Lösungen sowohl für Privatkunden, Geschäftskunden als auch Kommunen an, die schnell, fair und ohne Eigenleistung zu einer smarten Ladelösung für E-Fahrzeuge kommen möchten.</p>
    <p>Von der Beratung, über die Installation, Inbetriebnahme bis zur Abrechnung und Wartung bekommen Sie bei mero-kant alles aus einer Hand. Auf Wunsch vermieten wir auch die Ladetechnik und übernehmen im gewerblichen Bereich die direkte Abrechnung mit dem Nutzer. Für Kommunen bieten wir den kostenfreien Full-Service an und beteiligen die Gemeinden an der Nutzung der Infrastruktur.</p>
  </div>
  <a class="btn" href="#">WEITERLESEN</a>
  <div class="intro-visual"><div role="img" aria-label="Hand steckt Ladestecker in ein Fahrzeug, violett eingefärbt"></div></div>
  <div class="intro-object" role="img" aria-label="Weißer USB-Autoladeadapter"></div>
</section>

<section class="segment private">
  <div class="photo" role="img" aria-label="Mann mit Tablet lehnt an einem ladenden weißen Elektroauto"></div>
  <div class="content">
    <h3 class="display">Als <span class="accent">Privatkunde</span></h3>
    <ul class="checklist">
      <li>Bestandsanalyse mit umfangreicher Beratung über die Möglichkeiten der Umsetzung</li>
      <li>Prüfung und Übernahme der Anmeldung verfügbarer Fördermöglichkeiten</li>
      <li>Auswahl an smarten Wallbox Lösungen, passend für Ihr Fahrzeug und Ihre Bedürfnisse</li>
      <li>Installation inkl. aller notwendigen Materialien und Tätigkeiten (Durchbrüche, Erdarbeiten, etc.)</li>
    </ul>
    <a class="btn" href="#">WEITERLESEN</a>
  </div>
</section>

<section class="segment business">
  <div class="content">
    <h3 class="display">Als <span class="accent">Geschaftskunde</span></h3>
    <ul class="checklist">
      <li>Durchführung einer individuellen Bedarfsanalyse inkl. Ermittlung der Anforderungen für:
        <ul class="sublist">
          <li>Haus- und Immobilienverwaltungen</li>
          <li>Dienstleistungs- und Handelsunternehmen</li>
          <li>Hotel und Beherbergungsbetriebe</li>
          <li>Parkraum- und Parkhausbetreiber</li>
          <li>Tourismus, Sport- und Freizeiteinrichtungen</li>
        </ul>
      </li>
      <li>Planung und Projektierung des Installationsaufwands inkl. Materialverbrauch</li>
      <li>Leasing oder Kauf der Hardware</li>
    </ul>
    <a class="btn" href="#">WEITERLESEN</a>
  </div>
  <div class="photo" role="img" aria-label="Frau lädt ihr Elektroauto in einer Tiefgarage"></div>
</section>

<section class="segment community">
  <div class="photo" role="img" aria-label="Mann steckt Ladekabel in ein dunkles Elektroauto"></div>
  <div class="content">
    <h3 class="display">Als <span class="accent">Kommune</span></h3>
    <ul class="checklist">
      <li>Konzeptionierung möglicher Ladeinfrastrukturen innerhalb Ihrer Gemeinde</li>
      <li>Planung und Projektsteuerung inkl. sämtlicher behördlicher Genehmigungsverfahren und Beantragung von Fördermitteln</li>
      <li>Fachgerechte Installation und Inbetriebnahme</li>
      <li>Regelmäßige Wartung gemäß Vorschrif</li>
      <li>Reparatur und Kundenservice</li>
    </ul>
    <a class="btn" href="#">WEITERLESEN</a>
  </div>
</section>

<section class="products">
  <h2 class="display">Unsere <span class="accent">Produkte</span></h2>
  <div class="product-cards">
    <div class="product-card">Wallboxen für Einfamilienhäuser</div>
    <div class="product-card">Lösungen für Immobilienentwickler</div>
    <div class="product-card">All-in-One-Ladelösung für Kommunen</div>
    <div class="product-card">Lösungen für Tourismus/Hotels</div>
  </div>
</section>

<footer class="site-footer">
  <nav class="footer-nav">
    <a href="#">Lösungen</a>
    <a href="#">Unternehmen</a>
    <a href="#">Services</a>
    <a href="#">Karriere</a>
    <a href="#">Kontakt</a>
  </nav>
  <p class="copyright">Copyright © 2022 Mero-Kant De . Alle Rechte vorbehalten.</p>
  <div class="social"><span></span><span></span><span></span><span></span></div>
</footer>

</body>
</html>
```